Freeze Dried Raw Dog Food Label

Create a label for a Freeze Dried Raw dog and cat food line.
There are four flavors (beef, bison, fish and chicken).
4 x 8" Label FRONT AND BACK
Please see website www.morvelkitchen-example.com for our other product labels that this will need to stand next to.
Please use this color codes for the different flavors:
Chicken: #d5c55c
Beef: 469b9f
Bison: #275e6d
Fish: #a07980
The only other colors that should be used are Black, White, gray scale, and the shiny metallic gold as seen on our website: www.morvelkitchen-example.com
There will have 8 Variations:
Beef for dogs
Beef for Cats
Chicken for dogs
Chicken for cats
Bison for dogs
Bison for cats
Fish for dogs
Fish for cats.
There will be (2) 4X8 inch labels for each variation (a front side and a back side)
The Nutritional Information of the 4 flavors, is as follows:
BEEF
Ingredients
Beef, Beef Kidneys, Beef Hearts, Beef Liver, Whole Egg, Flaxseed, Organic Sweet Potato, Kelp, Organic Carrots, Organic Apples, Organic Blueberries, Cod Liver Oil, Pumpkin Seeds, Organic Spinach, Chicory Root, Organic Cranberries, Ginger, Mixed Tocopherols, Inulin, Dried Enterococcus faecium, Fermentation Product, Dried Lactobacillus acidophilus fermentation product
Calorie Content
Kcal/Cup 182
Guaranteed Analysis
Crude Protein – 38% (min)
Crude Fat – 36% (min)
Crude Fiber – 4% (max)
Moisture – 5% (max)
CHICKEN
Ingredients
Chicken, Chicken Liver, Chicken Hearts, Whole Egg, Flaxseed, Organic Sweet Potato, Kelp, Organic Carrots, Organic Apples, Organic Blueberries, Cod Liver Oil, Pumpkin Seeds, Organic Spinach, Chicory Root, Organic Cranberries, Ginger, Mixed Tocopherols, Inulin, Dried Enterococcus faecium, Fermentation Product, Dried Lactobacillus acidophilus fermentation product.
Calorie Content
Kcal/Cup 185
Guaranteed Analysis
Crude Protein – 45% (min)
Crude Fat – 34% (min)
Crude Fiber – 4% (max)
Moisture – 5% (max)
BISON:
Ingredients
Bison, Bison kidneys, Bison Livers, Whole Egg, Flaxseed, Organic Sweet Potato, Kelp, Organic Carrots, Organic Apples, Organic Blueberries, Cod Liver Oil, Pumpkin Seeds, Organic Spinach, Chicory Root, Organic Cranberries, Ginger, Mixed Tocopherols, Inulin, Dried Enterococcus faecium, Fermentation Product, Dried Lactobacillus acidophilus fermentation product.
Calorie Content
Kcal/Cup 186
Guaranteed Analysis
Crude Protein – 32% (min)
Crude Fat – 38% (min)
Crude Fiber – 5% (max)
Moisture – 5% (max)
FISH
Ingredients
Tuna, Salmon, Pollock, Whole Egg, Flaxseed, Organic Sweet Potato, Kelp, Organic Carrots, Organic Apples, Organic Blueberries, Cod Liver Oil, Pumpkin Seeds, Organic Spinach, Chicory Root, Organic Cranberries, Ginger, Mixed Tocopherols, Inulin, Dried Enterococcus faecium, Fermentation Product, Dried Lactobacillus acidophilus fermentation product.
Calorie Content
Kcal/Cup 455, Kcal/oz 114
Guaranteed Analysis
Crude Protein – 40% (min)
Crude Fat – 37% (min)
Crude Fiber – 4% (max)
Moisture – 5% (max)
THINGS TO ADD
Feeding Guidelines: Insert a QR CODE
Look and feel

```html
<!DOCTYPE html>
<html lang="en">
<head>
<meta charset="utf-8">
<title>Morvel Kitchen – Freeze Dried Raw Labels</title>
<link rel="stylesheet" href="https://fonts.googleapis.com/css2?family=Archivo+Black&family=Roboto:wght@300;400;500&display=swap">
<style>
  :root {
    --chicken: #d5c55c;
    --beef: #469b9f;
    --gold-light: #f1d68c;
    --gold: #c99a45;
    --gold-dark: #7a5520;
    --ink: #111111;
    --paper: #ffffff;
  }
  html, body {
    margin: 0;
    padding: 0;
    width: 1200px;
    height: 1200px;
    overflow: hidden;
    background: var(--paper);
  }
  .canvas {
    position: relative;
    width: 1200px;
    height: 1200px;
  }
  .label {
    position: absolute;
    top: 330px;
    width: 340px;
    height: 520px;
    box-shadow: 0 0 0 1px #ececec;
  }
  .label--dog { left: 180px; }
  .label--cat { left: 640px; }
  .label svg { display: block; width: 340px; height: 520px; }
  .brand-name {
    font-family: "Roboto", sans-serif;
    font-weight: 500;
    font-size: 30px;
    fill: var(--ink);
    letter-spacing: 0.5px;
  }
  .freeze {
    font-family: "Archivo Black", sans-serif;
    font-size: 30px;
    fill: var(--paper);
  }
  .dried-raw {
    font-family: "Roboto", sans-serif;
    font-weight: 300;
    font-size: 35px;
    fill: var(--paper);
  }
  .species {
    font-family: "Archivo Black", sans-serif;
    font-size: 14px;
    fill: var(--ink);
  }
  .flavor {
    font-family: "Archivo Black", sans-serif;
    font-size: 26px;
    fill: url(#goldVertical);
    stroke: var(--gold-dark);
    stroke-width: 0.6;
  }
</style>
</head>
<body>
<main class="canvas">
  <svg width="0" height="0" style="position:absolute" aria-hidden="true">
    <defs>
      <linearGradient id="goldSweep" x1="0" y1="1" x2="1" y2="0">
        <stop offset="0" stop-color="#7a5520"/>
        <stop offset="0.45" stop-color="#f1d68c"/>
        <stop offset="0.7" stop-color="#c99a45"/>
        <stop offset="1" stop-color="#f1d68c"/>
      </linearGradient>
      <linearGradient id="goldVertical" x1="0" y1="0" x2="0" y2="1">
        <stop offset="0" stop-color="#7a5520"/>
        <stop offset="0.5" stop-color="#c99a45"/>
        <stop offset="1" stop-color="#7a5520"/>
      </linearGradient>
      <radialGradient id="sketchTone" cx="0.5" cy="0.5" r="0.5">
        <stop offset="0" stop-color="#bdbdbd"/>
        <stop offset="1" stop-color="#ffffff" stop-opacity="0"/>
      </radialGradient>
    </defs>
  </svg>

  <section class="label label--dog">
    <svg viewBox="0 0 340 520">
      <rect width="340" height="520" fill="var(--paper)"/>
      <rect x="10" y="250" width="200" height="170" fill="url(#sketchTone)" role="img" aria-label="Pencil sketch of a dog's head"/>
      <path d="M340,165 C300,300 200,385 0,425 L0,520 L340,520 Z" fill="var(--chicken)"/>
      <path d="M340,165 C300,300 200,385 0,425" fill="none" stroke="url(#goldSweep)" stroke-width="6"/>
      <rect x="222" y="345" width="72" height="100" rx="10" fill="var(--ink)" opacity="0.85" role="img" aria-label="Black silhouette of a hen"/>
      <text class="flavor" transform="translate(328 372) rotate(-90)" textLength="140" lengthAdjust="spacingAndGlyphs">CHICKEN</text>
      <text class="brand-name" x="170" y="215" text-anchor="middle">Morvel Kitchen</text>
      <text class="freeze" x="12" y="470">Freeze</text>
      <text class="dried-raw" x="10" y="508">DRIED RAW</text>
      <text class="species" x="245" y="491">DOG</text>
      <text class="species" x="245" y="505">FOOD</text>
    </svg>
  </section>

  <section class="label label--cat">
    <svg viewBox="0 0 340 520">
      <rect width="340" height="520" fill="var(--paper)"/>
      <rect x="10" y="230" width="210" height="190" fill="url(#sketchTone)" role="img" aria-label="Pencil sketch of a tabby cat's head"/>
      <path d="M340,165 C300,300 200,385 0,425 L0,520 L340,520 Z" fill="var(--beef)"/>
      <path d="M340,165 C300,300 200,385 0,425" fill="none" stroke="url(#goldSweep)" stroke-width="6"/>
      <rect x="172" y="360" width="124" height="85" rx="10" fill="var(--ink)" opacity="0.85" role="img" aria-label="Black silhouette of a bull"/>
      <text class="flavor" transform="translate(328 440) rotate(-90)" textLength="84" lengthAdjust="spacingAndGlyphs">BEEF</text>
      <text class="brand-name" x="170" y="215" text-anchor="middle">Morvel Kitchen</text>
      <text class="freeze" x="12" y="470">Freeze</text>
      <text class="dried-raw" x="10" y="508">DRIED RAW</text>
      <text class="species" x="248" y="491">CAT</text>
      <text class="species" x="248" y="505">FOOD</text>
    </svg>
  </section>
</main>
</body>
</html>
```